Bakery Introducing a Crumbtastic Handcrafted Graham Cracker "Honey Crispets"

Though our Nibble On! brand name is well established, we're using our sister company's logo for this new product, as it fits better with the handcrafted artisan look we're going for. This "Marlow's Biscuits" logo is attached. The "Honey Crispets" are all natural, hand-crafted, and made with organic whole wheat flour. They will be packaged in two 6-packs in a stand-up, tin-tie top, resealable paper bag. Dimensions attached. The design needs to be 7 colors or less (including the logo), and either wrap around the entire bag, or be sectioned into panels. We'd like to emphasize the Honey Crispets all natural, butter-filled, deliciousness in a way that is warm, classic, and homey. Ideas & inspiration attached.
Updates

Target Market(s)

Shoppers at upscale grocery stores (Fresh Harvest, Larkspur Pantry, Verdant Provisions, etc.) who desire natural, local, handcrafted products.

Industry/Entity Type

It Company

Font styles to use
Serif
Decorative

Requirements
Must have
• Marlow's Biscuits Logo
• Honey Crispets
• Handcrafted
• All Natural
Nice to have
• Some way of emphasizing all the butter!
• Warm Colors
• A Vintage Feel

```html
<!DOCTYPE html>
<html lang="en">
<head>
<meta charset="utf-8">
<title>Honey Crispets – Bag Wrap</title>
<link href="https://fonts.googleapis.com/css2?family=Playfair+Display:wght@800;900&family=Libre+Baskerville:wght@400;700&display=swap" rel="stylesheet">
<style>
  :root {
    --paper: #ffffff;
    --brown: #3a1d0e;
    --brown-soft: #5a3418;
    --cream: #f4e4a6;
    --gold: #f7c325;
    --gold-deep: #eaa915;
    --red: #d23a1c;
    --white: #ffffff;
    --fold: #7a5a2a;
  }
  * { margin: 0; padding: 0; box-sizing: border-box; }
  html, body { width: 1200px; height: 1200px; overflow: hidden; background: var(--paper); }
  .canvas { position: relative; width: 1200px; height: 1200px; }

  .wrap {
    position: absolute; left: 104px; top: 250px; width: 1012px; height: 666px;
    background: linear-gradient(180deg, var(--gold) 0%, var(--gold-deep) 55%, var(--gold) 100%);
  }
  .band-top { position: absolute; left: 0; top: 0; width: 100%; height: 48px; background: var(--brown); }
  .scroll-border {
    position: absolute; left: 0; top: 48px; width: 100%; height: 74px;
    background: linear-gradient(180deg, var(--brown) 0%, var(--brown-soft) 35%, var(--cream) 60%, var(--gold) 100%);
  }
  .band-bottom {
    position: absolute; left: 0; bottom: 0; width: 100%; height: 32px; background: var(--brown);
    display: flex; justify-content: space-around; align-items: center; padding: 0 6px;
  }
  .band-bottom i { width: 5px; height: 5px; border-radius: 50%; background: var(--cream); display: block; }

  .fold { position: absolute; top: 0; width: 2px; height: 100%; background: var(--fold); opacity: .55; }

  .front { position: absolute; left: 0; top: 0; width: 290px; height: 100%; }
  .title {
    position: absolute; left: 18px; top: 198px;
    font-family: "Playfair Display", serif; font-weight: 900; font-size: 60px; line-height: 62px;
    color: var(--brown); text-shadow: 2px 2px 0 rgba(255,240,190,.6);
  }
  .title span { display: block; }
  .ribbon { position: absolute; left: 140px; top: 338px; width: 152px; height: 40px; transform: rotate(-5deg); }
  .ribbon-text {
    position: absolute; left: 0; top: 0; width: 100%; height: 32px; line-height: 32px; text-align: center;
    font-family: "Libre Baskerville", serif; font-weight: 700; font-size: 13px; letter-spacing: .5px; color: var(--white);
  }
  .window { position: absolute; left: 40px; top: 406px; width: 216px; height: 190px; background: var(--white); border-radius: 14px; }
  .handcrafted {
    position: absolute; left: 0; top: 610px; width: 290px; text-align: center;
    font-family: "Libre Baskerville", serif; font-weight: 700; font-size: 16px; letter-spacing: 2px; color: var(--brown);
  }

  .back { position: absolute; left: 506px; top: 0; width: 292px; height: 100%; }
  .wheat-mark {
    position: absolute; left: 118px; top: 268px; width: 56px; height: 104px; border-radius: 28px;
    background: linear-gradient(180deg, var(--brown-soft), var(--brown));
    opacity: .85;
  }
  .story {
    position: absolute; left: 28px; top: 398px; width: 240px; text-align: center;
    font-family: "Libre Baskerville", serif; font-size: 12.5px; line-height: 30px; color: var(--brown);
  }
  .maker {
    position: absolute; left: 46px; top: 502px; width: 210px; display: flex; align-items: center; justify-content: center; gap: 8px;
    font-family: "Libre Baskerville", serif; font-weight: 700; font-size: 17px; color: var(--brown);
  }
  .maker-dot { width: 16px; height: 16px; border-radius: 50%; background: var(--brown); flex: none; }
</style>
</head>
<body>
<div class="canvas">
  <div class="wrap">
    <div class="band-top"></div>
    <div class="scroll-border" role="img" aria-label="Cream scrollwork border along the top of the bag"></div>

    <div class="fold" style="left:290px"></div>
    <div class="fold" style="left:506px"></div>
    <div class="fold" style="left:798px"></div>

    <section class="front">
      <h1 class="title"><span>Honey</span><span>Crispets</span></h1>
      <div class="ribbon">
        <svg width="152" height="40" viewBox="0 0 152 40" aria-hidden="true">
          <polygon points="0,0 152,0 142,16 152,32 0,32 10,16" fill="var(--red)"/>
        </svg>
        <div class="ribbon-text">ALL NATURAL</div>
      </div>
      <div class="window"></div>
      <p class="handcrafted">HAND CRAFTED</p>
    </section>

    <section class="back">
      <div class="wheat-mark" role="img" aria-label="Wheat sheaf emblem"></div>
      <p class="story">The "Honey Crispets" are all natural,<br>hand-crafted, and made with organic<br>whole wheat flour.</p>
      <div class="maker"><span class="maker-dot"></span>Marlow's Biscuits</div>
    </section>

    <div class="band-bottom">
      <i></i><i></i><i></i><i></i><i></i><i></i><i></i><i></i><i></i><i></i><i></i><i></i><i></i><i></i><i></i><i></i><i></i><i></i><i></i><i></i><i></i><i></i><i></i><i></i><i></i><i></i><i></i><i></i><i></i><i></i><i></i><i></i><i></i><i></i><i></i><i></i><i></i><i></i><i></i><i></i><i></i><i></i><i></i><i></i><i></i><i></i><i></i><i></i><i></i><i></i>
    </div>
  </div>
</div>
</body>
</html>
```